Update Dulmar & Co Powerpoint to Quillmere Partnership

Hi, about 2 years ago I had a great Powerpoint template produced for my business called Dulmar & Co. We have now changed the company name and logo to Quillmere Partnership and I would like you to update the presentation template pages to the new logo and design.

I attach:

1) The original Powerpoint presentation that was produced for Dulmar
2) The new Quillmere Partnership logo files
3) The initial Powerpoint presentation format that my UK designer has done to give you an idea of their approach
4) The Font files (Red Hat Display - medium)

It would be great to receive the new PP template by Tuesday 22nd July.

Please message me if you have any questions.
Thanks
Ned

```html
<!DOCTYPE html>
<html lang="en">
<head>
<meta charset="utf-8">
<title>Quillmere Partnership – Presentation Template</title>
<link href="https://fonts.googleapis.com/css2?family=Red+Hat+Display:wght@400;500;600;700;800&display=swap" rel="stylesheet">
<style>
:root{
  --ink:#0f2a2f;
  --ink-deep:#0a2125;
  --orange:#d8401c;
  --orange-soft:#e9603a;
  --paper:#ffffff;
  --stage:#5e5e5e;
  --text:#333b3d;
  --muted:#6b7476;
}
*{margin:0;padding:0;box-sizing:border-box}
html,body{width:1078px;height:1200px;overflow:hidden}
body{background:linear-gradient(#5a5a5a,#656565);font-family:"Red Hat Display",sans-serif;color:var(--text);position:relative}
.slide{position:absolute;width:442px;height:249px;overflow:hidden;background:var(--paper);box-shadow:0 4px 14px rgba(0,0,0,.35)}
.col-l{left:89px}.col-r{left:547px}
.row-1{top:78px}.row-2{top:343px}.row-3{top:608px}.row-4{top:874px}
.dark{background:radial-gradient(circle at 55% 70%,#17434a 0,var(--ink) 55%,var(--ink-deep) 100%);color:#fff}

/* wordmark */
.brand{position:absolute;display:flex;align-items:center;gap:5px;font-weight:600;line-height:1}
.brand .dot{width:7px;height:7px;background:var(--orange)}
.brand .name{display:block;font-size:14px;color:var(--ink)}
.brand .sub{display:block;font-size:5.4px;letter-spacing:1.6px;color:var(--ink);margin-top:1px}
.brand.on-dark .name,.brand.on-dark .sub{color:#fff}
.brand.small{top:20px;right:19px}
.brand.small .name{font-size:13.5px}
.brand.large .dot{width:11px;height:11px}
.brand.large .name{font-size:29px}
.brand.large .sub{font-size:11px;letter-spacing:2.6px;margin-top:2px}

/* slide title */
.slide-title{position:absolute;left:37px;top:15px;font-size:18px;font-weight:600;color:var(--ink)}
.title-rule{position:absolute;left:0;top:27px;width:26px;height:1px;background:var(--ink)}
.title-rule::after{content:"";position:absolute;right:-2px;top:-2px;width:4px;height:4px;background:var(--orange);transform:rotate(45deg)}

/* footer */
.footer{position:absolute;right:0;bottom:0;width:278px;height:15px;background:var(--ink);color:#fff;font-size:6px;font-weight:700;display:flex;align-items:center;padding-left:31px;gap:4px}
.footer::before{content:"";position:absolute;left:-4px;top:0;width:14px;height:15px;background:var(--orange);transform:skewX(-40deg)}
.footer::after{content:"";position:absolute;left:6px;top:0;width:8px;height:15px;background:var(--paper);transform:skewX(-40deg)}
.footer svg{width:6px;height:6px;fill:var(--orange)}
.page-no{position:absolute;right:12px;bottom:9px;width:12px;height:12px;background:var(--orange);transform:rotate(45deg);box-shadow:0 0 0 1.5px #fff}
.page-no span{display:block;transform:rotate(-45deg);color:#fff;font-size:5px;font-weight:700;line-height:12px;text-align:center}

p.body{font-size:7px;line-height:13.5px;text-align:justify;color:var(--text)}
.photo{position:absolute}

/* cover */
.cover .brand{left:115px;top:30px}
.cover h1{position:absolute;left:0;right:0;top:115px;text-align:center;font-size:26px;font-weight:700;color:#fff}
.accent{color:var(--orange)}
.date-badge{position:absolute;left:182px;top:156px;width:77px;height:19px;background:var(--orange);color:#fff;font-size:9px;font-weight:700;text-align:center;line-height:19px}
.ring{position:absolute;border:1px solid rgba(120,180,185,.18);border-radius:50%}

/* services */
.service{position:absolute;top:50px;width:172px}
.service .photo{position:static;width:172px;height:92px}
.service h3{font-size:9px;font-weight:700;color:var(--ink);margin:13px 0 4px}

/* agenda */
.agenda-list{position:absolute;left:249px;top:60px;list-style:none}
.agenda-list li{display:flex;align-items:center;gap:10px;height:23.6px;font-size:9px;font-weight:500;color:var(--ink)}
.num{width:11px;height:11px;background:var(--orange);transform:rotate(45deg);flex:none}
.num span{display:block;transform:rotate(-45deg);color:#fff;font-size:4.5px;font-weight:700;line-height:11px;text-align:center}

/* why */
.why-copy{position:absolute;left:37px;top:48px;width:176px}
.why-list{position:absolute;left:37px;top:152px;list-style:none}
.why-list li{font-size:7.5px;font-weight:700;color:var(--ink);height:14px;display:flex;align-items:center;gap:6px}
.why-list li::before{content:"";width:4px;height:4px;background:var(--orange)}
.diamond-photo{position:absolute;transform:rotate(45deg)}

/* intro */
.intro-col{position:absolute;top:60px;width:176px}

/* how */
.step{position:absolute;display:flex;align-items:center;gap:14px;width:170px}
.step-icon{width:22px;height:22px;transform:rotate(45deg);flex:none;display:flex;align-items:center;justify-content:center;border:1.5px solid #fff;box-shadow:0 0 0 1.2px var(--ink)}
.step-icon.orange{background:var(--orange);box-shadow:0 0 0 1.2px var(--orange)}
.step-icon.navy{background:var(--ink)}
.step-icon svg{transform:rotate(-45deg);width:9px;height:9px;fill:#fff}
.step p{font-size:5.6px;line-height:10px;color:var(--text)}
.hub{position:absolute;left:192px;top:110px;width:46px;height:46px;border-radius:50%;background:var(--orange)}

/* divider & thanks */
.divider .brand{left:160px;top:18px}
.divider h2{position:absolute;left:0;right:0;top:114px;text-align:center;font-size:24px;font-weight:700;color:#fff}
.thanks .brand{left:140px;top:50px}
.thanks .contact{position:absolute;left:0;right:0;top:120px;text-align:center;font-size:9.5px;font-weight:600;color:#fff;display:flex;justify-content:center;align-items:center;gap:6px}
.thanks .contact svg{width:8px;height:8px;fill:var(--orange)}
.dots{position:absolute;left:6px;right:6px;top:148px;border-top:1.5px dotted rgba(255,255,255,.3)}
.thanks h2{position:absolute;left:0;right:0;top:155px;text-align:center;font-size:46px;font-weight:700;color:#fff;letter-spacing:-1px}
</style>
</head>
<body>

<svg width="0" height="0" style="position:absolute">
  <defs>
    <symbol id="i-phone" viewBox="0 0 24 24"><path d="M6.6 10.8a15 15 0 0 0 6.6 6.6l2.2-2.2c.3-.3.7-.4 1-.2 1.1.4 2.3.6 3.6.6.6 0 1 .4 1 1V20c0 .6-.4 1-1 1A17 17 0 0 1 3 4c0-.6.4-1 1-1h3.5c.6 0 1 .4 1 1 0 1.3.2 2.5.6 3.6.1.3 0 .7-.2 1z"/></symbol>
    <symbol id="i-mail" viewBox="0 0 24 24"><path d="M2 5h20v14H2zm2 2v.5l8 5 8-5V7z"/></symbol>
  </defs>
</svg>

<!-- Cover -->
<section class="slide dark cover col-l row-1">
  <div class="ring" style="left:100px;top:115px;width:240px;height:240px"></div>
  <div class="ring" style="left:140px;top:155px;width:160px;height:160px"></div>
  <div class="brand large on-dark"><span class="dot"></span><span><span class="name">Quillmere</span><span class="sub">PARTNERSHIP</span></span></div>
  <h1>Presentation <span class="accent">Title Goes</span> Here</h1>
  <div class="date-badge">JULY 18,2025</div>
</section>

<!-- Our Services -->
<section class="slide col-r row-1">
  <div class="title-rule"></div>
  <h2 class="slide-title">Our Services</h2>
  <div class="brand small"><span class="dot"></span><span><span class="name">Quillmere</span><span class="sub">PARTNERSHIP</span></span></div>
  <div class="service" style="left:33px">
    <div class="photo" role="img" aria-label="Photograph of colleagues meeting around a laptop in an office" style="background:linear-gradient(135deg,#3a3f44,#1c2226 60%,#4c4a47)"></div>
    <h3>Sed ut perspiciatis unde omni</h3>
    <p class="body">Sed ut perspiciatis unde omnis iste natus error sit voluptatem accusantium doloremque laudantium, totam rem aperiam, eaque ipsa quae ab illo inventore veritatis et quasi architecto beatae</p>
  </div>
  <div class="service" style="left:234px">
    <div class="photo" role="img" aria-label="Photograph of a business team standing together" style="background:linear-gradient(135deg,#8a9096,#3b4248 55%,#6c7278)"></div>
    <h3>Sed ut perspiciatis unde omni</h3>
    <p class="body">Sed ut perspiciatis unde omnis iste natus error sit voluptatem accusantium doloremque laudantium, totam rem aperiam, eaque ipsa quae ab illo inventore veritatis et quasi architecto beatae</p>
  </div>
  <div class="footer"><svg><use href="#i-phone"/></svg>Call Us : +1 555 010 0100 &nbsp;| &nbsp;<svg><use href="#i-mail"/></svg>info@quillmere.com</div>
  <div class="page-no"><span>05</span></div>
</section>

<!-- Agenda -->
<section class="slide col-l row-2">
  <div class="title-rule"></div>
  <h2 class="slide-title">Agenda</h2>
  <div class="brand small"><span class="dot"></span><span><span class="name">Quillmere</span><span class="sub">PARTNERSHIP</span></span></div>
  <div class="photo" role="img" aria-label="Team photograph with an orange duotone treatment" style="left:40px;top:60px;width:150px;height:150px;background:linear-gradient(135deg,var(--ink) 0,#3a2a24 45%,var(--orange) 100%)"></div>
  <ol class="agenda-list">
    <li><span class="num"><span>01</span></span>Introduction</li>
    <li><span class="num"><span>02</span></span>Sed ut perspiciatis unde omnis</li>
    <li><span class="num"><span>03</span></span>Iste natus error sit voluptatem</li>
    <li><span class="num"><span>04</span></span>Aaccusantium doloremque</li>
    <li><span class="num"><span>05</span></span>Laudantiumtotam rem aperiam</li>
    <li><span class="num"><span>06</span></span>Eaque ipsa quae ab illo</li>
    <li><span class="num"><span>07</span></span>Iinventore veritatis</li>
  </ol>
  <div class="footer"><svg><use href="#i-phone"/></svg>Call Us : +1 555 010 0100 &nbsp;| &nbsp;<svg><use href="#i-mail"/></svg>info@quillmere.com</div>
  <div class="page-no"><span>02</span></div>
</section>

<!-- Why Choose Us -->
<section class="slide col-r row-2">
  <div class="title-rule"></div>
  <h2 class="slide-title">Why Choose Us</h2>
  <div class="brand small"><span class="dot"></span><span><span class="name">Quillmere</span><span class="sub">PARTNERSHIP</span></span></div>
  <p class="body why-copy">Sed ut perspiciatis unde omnis iste natus error sit voluptatem accusantium doloremque laudantium, totam rem aperiam, eaque ipsa quae ab illo inventore veritatis et quasi architecto beataeed ut perspiciatis unde omnis iste natus error sit voluptatem accusantium doloremque laudantium, totam rem aperiam, eaque ipsa quae ab illo inventore veritatis et quasi</p>
  <ul class="why-list">
    <li>Sed ut perspiciatis unde omnrirspiciatis un</li>
    <li>Perspiciatis unde omnrirspiciatis un</li>
    <li>Ut perspiciatis unde omnrirspiciatis un</li>
    <li>Sed ut perspiciatis unde omnrirspiciatis un</li>
  </ul>
  <div class="diamond-photo" role="img" aria-label="Photograph of a presenter speaking to a meeting room" style="left:252px;top:69px;width:106px;height:106px;background:linear-gradient(135deg,#c9d3da,#56626c 60%,#2b343b)"></div>
  <div class="diamond-photo" role="img" aria-label="Photograph of smiling colleagues shaking hands, orange toned" style="left:335px;top:140px;width:106px;height:106px;background:linear-gradient(135deg,#f07a45,var(--orange) 55%,#8e2a10)"></div>
  <div class="footer"><svg><use href="#i-phone"/></svg>Call Us : +1 555 010 0100 &nbsp;| &nbsp;<svg><use href="#i-mail"/></svg>info@quillmere.com</div>
  <div class="page-no"><span>06</span></div>
</section>

<!-- Introduction -->
<section class="slide col-l row-3">
  <div class="title-rule"></div>
  <h2 class="slide-title">Introduction</h2>
  <div class="brand small"><span class="dot"></span><span><span class="name">Quillmere</span><span class="sub">PARTNERSHIP</span></span></div>
  <p class="body intro-col" style="left:37px">Sed ut perspiciatis unde omnis iste natus error sit voluptatem accusantium doloremque laudantium, totam rem aperiam, eaque ipsa quae ab illo inventore veritatis et quasi architecto beatae vitae dicta sunt explicabo. Nemo enim ipsam voluptatem quia voluptas sit aspernatur aut odit aut fugit, sed quia consequuntur magni dolores eos qui ratione voluptatem sequi nesciuneque porro quisquam est, qui doloquam eius modi tempora incidunt ut labore et dolore magnam aliquam quaerat voluptatem.</p>
  <p class="body intro-col" style="left:240px">Sed ut perspiciatis unde omnis iste natus error sit voluptatem accusantium doloremque laudantium, totam rem aperiam, eaque ipsa quae ab illo inventore veritatis et quasi architecto beatae vitae dicta sunt explicabo. Nemo enim ipsam voluptatem quia voluptas sit aspernatur aut odit aut fugit, sed quia consequuntur magni dolores eos qui ratione voluptatem sequi nesciuneque porro quisquam est, qui doloquam eius modi tempora incidunt ut labore et dolore magnam aliquam quaerat voluptatem.</p>
  <div class="footer"><svg><use href="#i-phone"/></svg>Call Us : +1 555 010 0100 &nbsp;| &nbsp;<svg><use href="#i-mail"/></svg>info@quillmere.com</div>
  <div class="page-no"><span>03</span></div>
</section>

<!-- How it Works -->
<section class="slide col-r row-3">
  <div class="title-rule"></div>
  <h2 class="slide-title">How it Works</h2>
  <div class="brand small"><span class="dot"></span><span><span class="name">Quillmere</span><span class="sub">PARTNERSHIP</span></span></div>
  <div class="step" style="left:26px;top:65px"><span class="step-icon navy"><svg viewBox="0 0 24 24"><path d="M9 4h6v3h6v13H3V7h6zm2 2v1h2V6z"/></svg></span><p>Sed ut perspiciatis unde omnis iste natus error sit voluptatemcusantium doloremque laudantium rem apeeaque ipsa quae</p></div>
  <div class="step" style="left:26px;top:115px"><span class="step-icon orange"><svg viewBox="0 0 24 24"><path d="M12 2l3 7h7l-5.5 4.5 2 7.5L12 16.5 5.5 21l2-7.5L2 9h7z"/></svg></span><p>Sed ut perspiciatis unde omnis iste natus error sit luptatemcusantium doloremque laudantium rem</p></div>
  <div class="step" style="left:26px;top:165px"><span class="step-icon navy"><svg viewBox="0 0 24 24"><path d="M12 2a10 10 0 1 0 0 20 10 10 0 0 0 0-20zm1 5v5l4 2-1 1.7-5-2.7V7z"/></svg></span><p>Sed ut perspiciatis unde omnis iste natus error sit voluptatemcusantium doloremque laudantium rem apeeaque ipsa quae</p></div>
  <div class="hub" aria-hidden="true"></div>
  <div class="step" style="left:262px;top:65px"><span class="step-icon orange"><svg viewBox="0 0 24 24"><circle cx="12" cy="8" r="4"/><circle cx="5" cy="10" r="3"/><circle cx="19" cy="10" r="3"/><path d="M4 20c0-4 4-6 8-6s8 2 8 6z"/></svg></span><p>Sed ut perspiciatis unde omnis iste natus error sit voluptatemcusantium doloremque laudantium rem apeeaque ipsa quae</p></div>
  <div class="step" style="left:262px;top:115px"><span class="step-icon navy"><svg viewBox="0 0 24 24"><path d="M6 2h12v20H6zm3 3v2h2V5zm4 0v2h2V5zm-4 4v2h2V9zm4 0v2h2V9zm-4 4v2h2v-2zm4 0v2h2v-2z"/></svg></span><p>Sed ut perspiciatis unde omnis iste natus error sit luptatemcusantium doloremque laudantium rem</p></div>
  <div class="step" style="left:262px;top:165px"><span class="step-icon orange"><svg viewBox="0 0 24 24"><path d="M2 4h20v13H13v2h4v2H7v-2h4v-2H2zm2 2v9h16V6z"/></svg></span><p>Sed ut perspiciatis unde omnis iste natus error sit voluptatemcusantium doloremque laudantium rem apeeaque ipsa quae</p></div>
  <div class="footer"><svg><use href="#i-phone"/></svg>Call Us : +1 555 010 0100 &nbsp;| &nbsp;<svg><use href="#i-mail"/></svg>info@quillmere.com</div>
  <div class="page-no"><span>07</span></div>
</section>

<!-- Section Divider -->
<section class="slide dark divider col-l row-4" role="img" aria-label="Dark-toned photograph of colleagues collaborating" style="background:linear-gradient(120deg,#0d2428 0,#1b3438 45%,#2a3e40 65%,#0f2a2f 100%)">
  <div class="brand on-dark"><span class="dot"></span><span><span class="name">Quillmere</span><span class="sub">PARTNERSHIP</span></span></div>
  <h2>Section <span class="accent">Divider</span> Title Here</h2>
</section>

<!-- Thank You -->
<section class="slide dark thanks col-r row-4" role="img" aria-label="Dark-toned photograph of a team at a conference table" style="background:linear-gradient(180deg,#16323a 0,#0f2a2f 55%,#0a1f23 100%)">
  <div class="brand large on-dark"><span class="dot"></span><span><span class="name">Quillmere</span><span class="sub">PARTNERSHIP</span></span></div>
  <div class="contact"><svg><use href="#i-phone"/></svg>Call Us : +1 555 010 0100 &nbsp;| &nbsp;<svg><use href="#i-mail"/></svg>info@quillmere.com</div>
  <div class="dots"></div>
  <h2>Thank <span class="accent">You</span></h2>
</section>

</body>
</html>
```